Whitby's Yard & Garden Center Business Card Update

I need an updated Business card design for my Lawn and Garden Center. We do Landscaping installs, Lawn Mowing, Snow Removal and also have a Garden Center Retail Division. I uploaded a few of our previous business cards to give an idea of what we are starting with. The main goal of this update is to simplify and modernize the business card, not all of the services that are on the previous cards has to be on the new one but I would still like to highlight our main services. There is also a sample of our logo that Can be used in the design.

Industry/Entity Type

Landscaping

Contact Information for Business Card

Desmond Whitby
Desmond@Whitbysyardandgarden.example
Business (555) 208-7316
Cell (555) 391-6842

Colors

Designer to choose colors to be used in the design.

Requirements
Must have
• Services Provided :
• Landscaping
• Lawn Maintenance
• Snow Removal
• Garden Center

```html
<!DOCTYPE html>
<html lang="en">
<head>
<meta charset="utf-8">
<title>Whitby's Yard &amp; Garden Center – Business Card</title>
<link href="https://fonts.googleapis.com/css2?family=Montserrat:wght@600;700&family=Open+Sans:wght@400;600;700&display=swap" rel="stylesheet">
<style>
  :root {
    --bg: #2a2a2a;
    --ink: #0b0b0c;
    --green: #2e5228;
    --paper: #ffffff;
    --text-dark: #161616;
  }
  * { box-sizing: border-box; margin: 0; padding: 0; }
  html, body { width: 1200px; height: 900px; overflow: hidden; }
  body {
    background: var(--bg);
    font-family: "Open Sans", Arial, sans-serif;
    position: relative;
  }
  .card {
    position: absolute;
    left: 260px;
    width: 680px;
    height: 388px;
    overflow: hidden;
  }
  /* Back side */
  .card-back { top: 46px; background: var(--ink); }
  .card-back .band {
    position: absolute; left: 0; right: 0; top: 190px; bottom: 0;
    background: var(--green);
  }
  .card-back .rule {
    position: absolute; left: 0; right: 0; height: 2px; background: var(--ink);
  }
  .card-back .rule.top { top: 212px; }
  .card-back .rule.bottom { top: 360px; }
  .card-back .brand {
    position: absolute; left: 0; right: 0; top: 96px;
    text-align: center;
    font-weight: 700; font-size: 54px; color: var(--paper);
    display: flex; align-items: center; justify-content: center; gap: 16px;
  }
  .brand-mark { width: 22px; height: 22px; background: var(--green); }
  .services {
    position: absolute; left: 0; right: 0; top: 228px; text-align: center;
  }
  .services h2 {
    font-size: 15px; font-weight: 700; letter-spacing: 0.5px; color: var(--ink);
    margin-bottom: 10px;
  }
  .services ul { list-style: none; }
  .services li {
    font-size: 17px; line-height: 23px; color: var(--paper); letter-spacing: 0.5px;
  }
  /* Front side */
  .card-front { top: 466px; background: var(--paper); }
  .card-front .brand {
    position: absolute; left: 56px; top: 46px;
    font-weight: 700; font-size: 52px; color: var(--text-dark);
    display: flex; align-items: center; gap: 14px;
  }
  .card-front .company {
    position: absolute; left: 58px; top: 124px;
    font-family: "Montserrat", Arial, sans-serif;
    font-weight: 700; font-size: 12px; letter-spacing: 0.6px; color: var(--text-dark);
  }
  .card-front .person {
    position: absolute; left: 56px; top: 150px;
    font-family: "Montserrat", Arial, sans-serif;
    font-weight: 700; font-size: 30px; letter-spacing: 1px; color: var(--green);
  }
  .card-front .divider {
    position: absolute; left: 50px; right: 40px; top: 198px; height: 2px;
    background: var(--green);
  }
  .contacts {
    position: absolute; left: 56px; top: 216px; list-style: none;
  }
  .contacts li {
    display: flex; align-items: center; gap: 10px;
    font-size: 19px; line-height: 26px; color: var(--text-dark);
  }
  .contacts svg { width: 16px; height: 16px; flex: none; }
  .footer-green, .footer-dark { position: absolute; left: 0; bottom: 0; }
</style>
</head>
<body>

<section class="card card-back" aria-label="Business card back">
  <div class="band"></div>
  <div class="rule top"></div>
  <div class="rule bottom"></div>
  <div class="brand"><span class="brand-mark"></span>Whitby's</div>
  <div class="services">
    <h2>SERVICES PROVIDED</h2>
    <ul>
      <li>LANDSCAPING</li>
      <li>LAWN MAINTENANCE</li>
      <li>SNOW REMOVAL</li>
      <li>GARDEN CENTER</li>
    </ul>
  </div>
</section>

<section class="card card-front" aria-label="Business card front">
  <div class="brand"><span class="brand-mark"></span>Whitby's</div>
  <div class="company">WHITBY'S YARD &amp; GARDEN CENTER</div>
  <div class="person">DESMOND WHITBY</div>
  <div class="divider"></div>
  <ul class="contacts">
    <li>
      <svg viewBox="0 0 16 16" fill="none" stroke="#2e5228" stroke-width="1.4">
        <circle cx="8" cy="8" r="6.5"/>
        <path d="M5.5 5 Q5 8 8 10.5 Q10 11.5 10.8 10.5"/>
      </svg>
      (555) 208-7316
    </li>
    <li>
      <svg viewBox="0 0 16 16" fill="none" stroke="#2e5228" stroke-width="1.4">
        <rect x="4.5" y="1.5" width="7" height="13" rx="1.2"/>
        <line x1="7" y1="12.3" x2="9" y2="12.3"/>
      </svg>
      (555) 391-6842
    </li>
    <li>
      <svg viewBox="0 0 16 16" fill="none" stroke="#2e5228" stroke-width="1.4">
        <rect x="1.5" y="3.5" width="13" height="9"/>
        <path d="M1.5 3.5 L8 9 L14.5 3.5"/>
      </svg>
      Desmond@Whitbysyardandgarden.example
    </li>
  </ul>
  <svg class="footer-dark" width="680" height="70" viewBox="0 0 680 70" aria-hidden="true">
    <polygon points="0,42 680,42 680,70 0,70" fill="#0b0b0c"/>
  </svg>
  <svg class="footer-green" width="680" height="70" viewBox="0 0 680 70" aria-hidden="true">
    <polygon points="0,0 440,0 470,70 0,70" fill="#2e5228"/>
  </svg>
</section>

</body>
</html>
```